現在ホームページリニューアルを検討しております。
社内でのデザインだとどうしても前情報がある分、発想の限界、偏りがどうしてもあります。

今回はなるべくフラットな状態でデザインを検討したいと考えておりますので、こちらで公募をさせていただくことにしました。

既存の歯科医院のデザインやイメージに縛られることなく、自由な発想でご提案頂きたいと思っております。

■依頼内容

PC・スマートフォン用 それぞれ1枚 合計2枚
(実装する際にはレスポンシブの予定です。)

診療科目は
小児
一般
矯正(大学から月に数回先生にお越し頂いています)

医院の特徴
ショッピングモール内にあります
駐車場あり
バリアフリー
お子さんの遊びスペースあり
デザイナー物件

ページ数
2ページ
希望イメージ
シンプル 複雑
単色 カラフル
暗い 明るい
日常 高級
遊び心 厳粛
未来的 伝統的
女性的 男性的
納品ファイル
• 高解像度JPG (.jpg)
• フォトショップ形式 (.psd)
• PNG形式 (.png)
▼弊社が用意するもの
・ページ構成
・テキスト
・ワイヤーフレーム
・ロゴ
・写真
※受注者様のご意向があれば、ビデオ通話などで対応することも可能です。
※ページ構成や画像などは、個別に送らせていただきたいので、まずはご提案またはメッセージにてご連絡ください。

▼依頼の流れ
1.ご提案
ご提案をいただき次第、弊社よりTOPページの構成をお送りします。
3.デザイン作成
デザインを作成しましたら、提案の【追記する】からデザインファイルの追加をしてください。
5.修正依頼
修正していただきたい箇所がある場合は、修正依頼をいたしますので、修正案を再提案してください。
6.納品
フォトショップ(psd)またはイラストレーター(ai)形式で納品をしていただきます。納品が完了次第、当選を行います。

弊社では、複数のWEBサイトを運用しております。
今回はTOPページのみの依頼となっておりますが、継続的に依頼をさせていただくことも考えております。
ご提案をお待ちしております。
ワイヤーフレームと写真素材を添付します。
依頼金額を45000円に変更して、延長しました。
たくさんのご応募ありがとうございます。
現在、選考中です。3~7日程度で当選デザインを決定できるかと思いますので、今しばらくお待ちください。

歯科医院スタッフの投票にて決定いたしました。

たくさんのご提案ありがとうございます。また機会があれば、是非よろしくお願いいたします。

```html
<!DOCTYPE html>
<html lang="ja">
<head>
<meta charset="utf-8">
<title>歯科医院 トップページ</title>
<link href="https://fonts.googleapis.com/css2?family=Noto+Sans+JP:wght@400;500;700&family=Noto+Serif+JP:wght@500;700;900&family=Cinzel+Decorative:wght@700&display=swap" rel="stylesheet">
<style>
:root{
  --mint:#e3f5dc;
  --mint-deep:#cdebc3;
  --green:#3fae55;
  --green-dark:#2f8f46;
  --nav:#5d9d6b;
  --cream:#fffbdc;
  --cream-line:#e9e2a8;
  --ink:#333;
  --muted:#666;
  --white:#fff;
}
*{box-sizing:border-box;margin:0;padding:0}
html,body{width:1200px;height:5172px;overflow:hidden}
body{background:var(--mint);font-family:"Noto Sans JP",sans-serif;color:var(--ink);position:relative}
.photo{position:absolute;border-radius:2px}

/* header */
.site-header{position:absolute;left:0;top:0;width:1200px;height:120px;background:var(--mint)}
.logo-box{position:absolute;left:130px;top:28px;width:270px;height:58px;border:2px solid var(--green);background:var(--white);display:flex;align-items:center;justify-content:center;font-size:22px;color:var(--green-dark);font-weight:500}
.header-phone{position:absolute;left:660px;top:14px;font-size:26px;font-weight:700;color:var(--green-dark);display:flex;align-items:center;gap:8px;white-space:nowrap}
.btn{display:flex;align-items:center;justify-content:center;background:var(--green);color:var(--white);font-weight:700;border-radius:4px;white-space:nowrap}
.header-btn{position:absolute;left:660px;top:60px;width:200px;height:40px;font-size:17px}
.header-hours{position:absolute;left:910px;top:20px;font-size:17px;line-height:34px;color:var(--green-dark);white-space:nowrap}

/* hero */
.hero{position:absolute;left:0;top:120px;width:1200px;height:520px}
.hero .photo{left:0;top:0;width:1200px;height:520px;background:linear-gradient(100deg,#eef4f3 0%,#dbe8ea 40%,#f4f7f6 75%,#e7eeee 100%)}
.hero-title{position:absolute;left:660px;top:96px;font-family:"Noto Serif JP",serif;font-weight:900;font-size:58px;color:var(--white);text-shadow:0 0 10px rgba(0,100,60,.45);white-space:nowrap}
.hero-btn{position:absolute;left:910px;top:392px;width:254px;height:46px;font-size:15px;border-radius:2px;border:2px solid var(--white)}
.hero-arrow{position:absolute;top:220px}
.hero-dots{position:absolute;left:564px;top:490px;display:flex;gap:14px}
.hero-dots span{width:12px;height:12px;border-radius:50%;background:#c6d8cc}
.hero-dots span.on{background:var(--green)}

/* banner thumbs */
.thumbs{position:absolute;left:0;top:640px;width:1200px;height:100px;background:var(--mint);display:flex;justify-content:center;align-items:center;gap:14px}
.thumb{width:148px;height:68px;border:3px solid var(--white);background:linear-gradient(120deg,#dff0e2,#bfd9cf)}
.thumb.on{border-color:var(--green)}

/* nav */
.global-nav{position:absolute;left:0;top:740px;width:1200px;height:52px;background:var(--nav);display:flex;align-items:center;justify-content:center}
.global-nav a{color:var(--white);text-decoration:none;font-size:16px;font-weight:500;padding:0 20px;border-left:1px solid rgba(255,255,255,.7);line-height:18px}
.global-nav a:first-child{border-left:none}
.interior{left:0;top:792px;width:1200px;height:268px;background:linear-gradient(90deg,#e9ece8,#f7f8f4 30%,#dfe5df 60%,#f2f3ee 100%)}

/* section titles */
.sec-title{position:absolute;left:0;width:1200px;display:flex;align-items:center;justify-content:center;gap:20px;z-index:3}
.sec-title .line{width:130px;height:3px;background:var(--green)}
.sec-title .pill{background:var(--green);color:var(--white);font-family:"Noto Serif JP",serif;font-weight:900;font-size:40px;padding:2px 36px;border-radius:30px;letter-spacing:4px;white-space:nowrap}
.sec-title .pill.en{font-family:"Cinzel Decorative",serif;font-size:36px;letter-spacing:2px}

/* treatment */
.treat-bg{position:absolute;left:0;top:1060px;width:1200px;height:1430px;background:var(--mint)}
.cat-box{position:absolute;left:280px;top:1250px;width:640px;height:270px;background:var(--cream);border:2px solid #b9ddb0;border-radius:36px;z-index:2}
.cat{position:absolute;top:24px;width:200px;text-align:center}
.cat h3{font-family:"Noto Serif JP",serif;font-weight:900;font-size:30px;color:var(--green-dark)}
.cat p{font-size:11px;line-height:16px;color:var(--muted);margin-top:6px}
.trap{position:absolute;left:130px;top:1500px;width:940px;height:240px}
.content-label{position:absolute;left:480px;top:1668px;width:240px;height:50px;border-radius:25px;background:var(--green);color:var(--white);font-family:"Noto Serif JP",serif;font-weight:900;font-size:32px;display:flex;align-items:center;justify-content:center;z-index:2}
.grid{position:absolute;left:150px;top:1748px;width:900px;height:712px;background:var(--cream);border:2px solid var(--cream-line);display:grid;grid-template-columns:repeat(3,1fr);grid-template-rows:repeat(3,1fr)}
.item{border:1px solid var(--cream-line);padding:8px 18px 0;text-align:center;overflow:hidden}
.item h4{font-family:"Noto Serif JP",serif;font-size:18px;color:var(--green-dark);font-weight:700;margin-bottom:6px}
.item .pic{height:140px;background:linear-gradient(130deg,#f0e6dc,#d8e7ec)}
.item p{text-align:left;font-size:11px;line-height:16px;color:var(--muted);margin-top:8px}

/* concept */
.concept-bg{position:absolute;left:0;top:2490px;width:1200px;height:1590px;background:linear-gradient(#d6efcd,#e6f6e0 30%,#eef9ea)}
.concept-card{position:absolute;top:2620px;width:270px;height:280px;border-radius:50%;background:var(--white);border:3px solid #a9d9a0;text-align:center}
.concept-card .ic{margin:30px auto 0;display:block}
.concept-card p{font-size:20px;line-height:30px;color:var(--ink);margin-top:12px}
.small-btn{position:absolute;left:98px;bottom:44px;width:74px;height:28px;font-size:13px;border-radius:3px}
.feature-label{position:absolute;left:510px;top:3006px;width:180px;height:44px;border-radius:4px;background:var(--green);color:var(--white);display:flex;align-items:center;justify-content:center;font-size:22px;font-family:"Noto Serif JP",serif;font-weight:700}
.feature{position:absolute;width:240px;height:240px;border-radius:50%;background:var(--white);border:3px solid #b3dcab;text-align:center}
.feature svg{margin:38px auto 0;display:block}
.feature p{font-size:16px;line-height:22px;color:var(--green-dark);font-weight:500;margin-top:8px}

/* news */
.news-box{position:absolute;left:320px;top:3720px;width:600px;height:300px;background:var(--white);border:2px solid #cfd8cd;border-radius:14px;padding:22px 36px;font-size:15px;line-height:27px;color:var(--muted)}
.news-box li{list-style:none;display:flex;gap:14px;font-family:"Noto Serif JP",serif;white-space:nowrap}

/* greeting */
.greet-bg{position:absolute;left:0;top:4080px;width:1200px;height:580px;background:#cbeac1}
.greet-card{position:absolute;left:140px;top:4240px;width:920px;height:340px;background:var(--white)}
.greet-photo{left:152px;top:4258px;width:388px;height:282px;background:linear-gradient(120deg,#e7f1f4,#cfe2ea 50%,#f0f5f2)}
.greet-text{position:absolute;left:580px;top:4280px;width:450px;font-size:13px;line-height:24px;color:var(--muted)}
.greet-sign{text-align:right;margin-top:26px}

/* footer */
.site-footer{position:absolute;left:0;top:4660px;width:1200px;height:512px;background:var(--mint)}
.foot-logo{left:100px;top:4694px;width:420px;height:56px}
.foot-addr{position:absolute;left:150px;top:4782px;font-size:15px;line-height:28px;color:var(--muted)}
.foot-phone{position:absolute;left:150px;top:4844px;font-size:30px;font-weight:700;color:var(--green-dark);display:flex;align-items:center;gap:8px}
.foot-btn{position:absolute;left:150px;top:4920px;width:310px;height:60px;font-size:22px}
.sched{position:absolute;left:640px;top:4704px;width:520px;background:var(--white);border-collapse:collapse;font-size:15px}
.sched th,.sched td{border:1px solid #8a8a8a;height:52px;text-align:center;font-weight:400}
.sched-note{position:absolute;left:645px;top:4870px;font-size:14px;line-height:24px;color:var(--ink)}
.foot-nav{position:absolute;left:0;top:5066px;width:1200px;display:flex;justify-content:center}
.foot-nav a{color:var(--green-dark);text-decoration:none;font-size:15px;padding:0 18px;border-left:1px solid var(--green-dark);line-height:16px}
.foot-nav a:first-child{border-left:none}
.copyright{position:absolute;left:0;top:5126px;width:1200px;text-align:center;font-size:12px;color:var(--muted);font-family:"Noto Serif JP",serif}
</style>
</head>
<body>

<header class="site-header">
  <div class="logo-box">LOGO・歯科医院名</div>
  <div class="header-phone">
    <svg width="22" height="22" viewBox="0 0 24 24"><path fill="#2f8f46" d="M6.6 10.8a15 15 0 0 0 6.6 6.6l2.2-2.2a1 1 0 0 1 1-.25 11 11 0 0 0 3.6.6 1 1 0 0 1 1 1V20a1 1 0 0 1-1 1A17 17 0 0 1 3 4a1 1 0 0 1 1-1h3.5a1 1 0 0 1 1 1c0 1.25.2 2.45.6 3.6a1 1 0 0 1-.25 1z"/></svg>
    123−456−7890
  </div>
  <div class="btn header-btn">Web 予約はこちら</div>
  <div class="header-hours">診療時間／9：00 ～ 20:00<br>休診日／木曜・日曜・祝日</div>
</header>

<section class="hero">
  <div class="photo" role="img" aria-label="歯科医師が患者を診療している写真"></div>
  <div class="hero-title">痛くない歯科治療</div>
  <div class="btn hero-btn">医療シュミレーションはこちら</div>
  <svg class="hero-arrow" style="left:30px" width="30" height="60" viewBox="0 0 30 60"><path d="M24 6 6 30l18 24" stroke="#fff" stroke-width="5" fill="none"/></svg>
  <svg class="hero-arrow" style="left:1140px" width="30" height="60" viewBox="0 0 30 60"><path d="M6 6l18 24L6 54" stroke="#fff" stroke-width="5" fill="none"/></svg>
  <div class="hero-dots"><span class="on"></span><span></span><span></span></div>
</section>

<div class="thumbs">
  <div class="thumb" role="img" aria-label="スライド1の縮小画像"></div>
  <div class="thumb on" role="img" aria-label="スライド2の縮小画像"></div>
  <div class="thumb" role="img" aria-label="スライド3の縮小画像"></div>
</div>

<nav class="global-nav">
  <a>HOME</a><a>初めての方へ</a><a>小児</a><a>一般</a><a>矯正</a><a>診療内容</a><a>コンセプト</a><a>アクセス</a>
</nav>
<div class="photo interior" role="img" aria-label="明るい白基調の院内診療室の写真"></div>

<section class="treat-bg"></section>
<div class="sec-title" style="top:1160px"><span class="line"></span><span class="pill">治療科目</span><span class="line"></span></div>

<svg class="trap" viewBox="0 0 940 240" preserveAspectRatio="none"><polygon points="160,0 780,0 940,240 0,240" fill="#fffbdc"/></svg>

<div class="cat-box">
  <div class="cat" style="left:14px"><h3>小児</h3>
    <svg width="60" height="70" viewBox="0 0 60 70" style="margin-top:10px"><circle cx="30" cy="10" r="8" fill="#3fae55"/><path d="M18 22h24l8 14-6 3-6-9v12l6 24h-8l-6-18-6 18h-8l6-24V30l-6 9-6-3z" fill="#3fae55"/></svg>
  </div>
  <div class="cat" style="left:220px"><h3>一般</h3>
    <svg width="80" height="60" viewBox="0 0 80 60" style="margin-top:18px"><circle cx="20" cy="16" r="8" fill="#3fae55"/><circle cx="60" cy="16" r="8" fill="#3fae55"/><circle cx="40" cy="12" r="9" fill="#3fae55"/><path d="M6 42a14 12 0 0 1 28 0v6H6zM46 42a14 12 0 0 1 28 0v6H46z" fill="#3fae55"/><path d="M24 40a16 14 0 0 1 32 0v8H24z" fill="#2f8f46"/></svg>
  </div>
  <div class="cat" style="left:426px"><h3>矯正</h3>
    <svg width="110" height="80" viewBox="0 0 110 80" style="position:absolute;left:0;top:58px"><circle cx="30" cy="18" r="11" fill="#3fae55"/><path d="M10 56a20 18 0 0 1 40 0v8H10z" fill="#3fae55"/><path d="M76 22c6-4 12-4 18 0 4 3 2 14-2 26-2 6-6 6-7 0l-1-8-2 8c-1 6-5 6-7 0-4-12-5-22 1-26z" fill="none" stroke="#3fae55" stroke-width="3"/></svg>
    <p style="margin-left:112px;text-align:left">大学から月に数回<br>先生にお越し<br>頂いています</p>
  </div>
</div>

<div class="content-label">治療内容</div>
<div class="grid">
  <div class="item"><h4>治療名 1</h4><div class="pic" role="img" aria-label="小児歯科の診療写真"></div><p>ここに治療内容の説明が入ります。ここに治療内容の説明が入ります。</p></div>
  <div class="item"><h4>治療名 2</h4><div class="pic" role="img" aria-label="歯科器具の写真"></div><p>ここに治療内容の説明が入ります。ここに治療内容の説明が入ります。</p></div>
  <div class="item"><h4>治療名 3</h4><div class="pic" role="img" aria-label="口元のクローズアップ写真"></div><p>ここに治療内容の説明が入ります。ここに治療内容の説明が入ります。</p></div>
  <div class="item"><h4>治療名 4</h4><div class="pic" role="img" aria-label="歯の模型の写真"></div><p>ここに治療内容の説明が入ります。ここに治療内容の説明が入ります。</p></div>
  <div class="item"><h4>治療名 5</h4><div class="pic" role="img" aria-label="笑顔の口元の写真"></div><p>ここに治療内容の説明が入ります。ここに治療内容の説明が入ります。</p></div>
  <div class="item"><h4>治療名 6</h4><div class="pic" role="img" aria-label="入れ歯の写真"></div><p>ここに治療内容の説明が入ります。ここに治療内容の説明が入ります。</p></div>
  <div class="item"><h4>治療名 7</h4><div class="pic" role="img" aria-label="歯磨き指導の写真"></div><p>ここに治療内容の説明が入ります。ここに治療内容の説明が入ります。</p></div>
  <div class="item"><h4>治療名 8</h4><div class="pic" role="img" aria-label="歯科用ミラーと器具の写真"></div><p>ここに治療内容の説明が入ります。ここに治療内容の説明が入ります。</p></div>
  <div class="item"><h4>治療名 9</h4><div class="pic" role="img" aria-label="診療チェアの写真"></div><p>ここに治療内容の説明が入ります。ここに治療内容の説明が入ります。</p></div>
</div>

<section class="concept-bg"></section>
<div class="sec-title" style="top:2510px"><span class="line"></span><span class="pill en">Concept</span><span class="line"></span></div>

<div class="concept-card" style="left:130px">
  <svg class="ic" width="60" height="60" viewBox="0 0 60 60"><circle cx="30" cy="30" r="26" fill="none" stroke="#3fae55" stroke-width="3"/><circle cx="21" cy="24" r="3" fill="#3fae55"/><circle cx="39" cy="24" r="3" fill="#3fae55"/><path d="M18 36q12 12 24 0" fill="none" stroke="#3fae55" stroke-width="3"/></svg>
  <p>痛くない歯科治療</p>
  <div class="btn small-btn">詳細 ▸</div>
</div>
<div class="concept-card" style="left:465px">
  <svg class="ic" width="60" height="60" viewBox="0 0 60 60"><circle cx="30" cy="30" r="26" fill="none" stroke="#3fae55" stroke-width="3"/><circle cx="24" cy="22" r="6" fill="none" stroke="#3fae55" stroke-width="3"/><circle cx="38" cy="30" r="5" fill="none" stroke="#3fae55" stroke-width="3"/><path d="M14 46q10-14 20 0M32 46q6-8 12 0" fill="none" stroke="#3fae55" stroke-width="3"/></svg>
  <p>お子様連れでも安心な<br>託児サービス</p>
  <div class="btn small-btn">詳細 ▸</div>
</div>
<div class="concept-card" style="left:800px">
  <svg class="ic" width="60" height="60" viewBox="0 0 60 60"><circle cx="30" cy="30" r="26" fill="none" stroke="#3fae55" stroke-width="3"/><path d="M14 34l4-10h24l4 10v8H14z" fill="none" stroke="#3fae55" stroke-width="3"/><circle cx="21" cy="42" r="3" fill="#3fae55"/><circle cx="39" cy="42" r="3" fill="#3fae55"/></svg>
  <p>何度も通院させない<br>歯医者さん</p>
  <div class="btn small-btn">詳細 ▸</div>
</div>

<div class="feature-label">医院の特徴</div>
<div class="feature" style="left:200px;top:3080px">
  <svg width="90" height="80" viewBox="0 0 90 80"><path d="M4 8h14l10 40h46l10-30H24" fill="none" stroke="#3fae55" stroke-width="8" stroke-linejoin="round"/><rect x="28" y="22" width="50" height="22" fill="#3fae55"/><circle cx="34" cy="66" r="7" fill="#3fae55"/><circle cx="70" cy="66" r="7" fill="#3fae55"/></svg>
  <p>ショッピング<br>モール内にあり</p>
</div>
<div class="feature" style="left:480px;top:3080px">
  <svg width="90" height="80" viewBox="0 0 90 80"><path d="M12 44l8-26q2-6 8-6h34q6 0 8 6l8 26v20H12z" fill="#3fae55"/><rect x="24" y="20" width="42" height="18" fill="#fff"/><circle cx="24" cy="52" r="5" fill="#fff"/><circle cx="66" cy="52" r="5" fill="#fff"/><rect x="14" y="62" width="12" height="12" fill="#3fae55"/><rect x="64" y="62" width="12" height="12" fill="#3fae55"/></svg>
  <p>駐車場あり</p>
</div>
<div class="feature" style="left:760px;top:3080px">
  <svg width="90" height="80" viewBox="0 0 90 80"><circle cx="45" cy="24" r="18" fill="#3fae55"/><path d="M26 52q19-14 38 0l6 22H20z" fill="#3fae55"/><path d="M14 50l12-6M76 50l-12-6" stroke="#3fae55" stroke-width="7" stroke-linecap="round"/></svg>
  <p>あかちゃんの<br>遊びスペースあり</p>
</div>
<div class="feature" style="left:340px;top:3340px">
  <svg width="80" height="80" viewBox="0 0 80 80"><rect width="80" height="80" rx="6" fill="#3fae55"/><circle cx="38" cy="14" r="6" fill="#fff"/><path d="M34 24v22h18l8 16" fill="none" stroke="#fff" stroke-width="6" stroke-linecap="round"/><path d="M26 36a16 16 0 1 0 24 20" fill="none" stroke="#fff" stroke-width="5"/></svg>
  <p>バリアフリー</p>
</div>
<div class="feature" style="left:620px;top:3340px">
  <svg width="90" height="80" viewBox="0 0 90 80"><path d="M6 40 45 8l39 32" fill="none" stroke="#3fae55" stroke-width="8" stroke-linejoin="round"/><path d="M16 38v36h58V38" fill="none" stroke="#3fae55" stroke-width="6"/><path d="M33 50q12 10 24 0" fill="none" stroke="#3fae55" stroke-width="5"/></svg>
  <p>デザイナー物件</p>
</div>

<div class="sec-title" style="top:3620px"><span class="line"></span><span class="pill">お知らせ</span><span class="line"></span></div>
<ul class="news-box">
  <li><span>2019/10/10</span><span>text text text text text text text text</span></li>
  <li><span>2019/10/01</span><span>text text text text text text text text</span></li>
  <li><span>2019/09/20</span><span>text text text text text text text text</span></li>
  <li><span>2019/09/12</span><span>text text text text text text text text</span></li>
  <li><span>2019/08/18</span><span>text text text text text text text text</span></li>
  <li><span>2019/07/30</span><span>text text text text text text text text</span></li>
  <li><span>2019/04/20</span><span>text text text text text text text text</span></li>
  <li><span>2019/03/10</span><span>text text text text text text text text</span></li>
  <li><span>2019/02/25</span><span>text text text text text text text text</span></li>
</ul>

<section class="greet-bg"></section>
<div class="sec-title" style="top:4140px"><span class="line"></span><span class="pill">ごあいさつ</span><span class="line"></span></div>
<div class="greet-card"></div>
<div class="photo greet-photo" role="img" aria-label="白衣を着た院長とスタッフの写真"></div>
<div class="greet-text">
  <p style="margin-bottom:14px">地域の皆さまのご健康を</p>
  <p>ごあいさつ文がここに入ります。ごあいさつ文がここに入ります。ごあいさつ文がここに入ります。ごあいさつ文がここに入ります。ごあいさつ文がここに入ります。ごあいさつ文がここに入ります。</p>
  <p class="greet-sign">○○歯科クリニック<br>院長 ○○ ○○</p>
</div>

<footer class="site-footer"></footer>
<div class="logo-box foot-logo">LOGO・歯科医院名</div>
<div class="foot-addr">〒000-0000<br>○○県○○市○○町○－○－○ 123-456</div>
<div class="foot-phone">
  <svg width="26" height="26" viewBox="0 0 24 24"><path fill="#2f8f46" d="M6.6 10.8a15 15 0 0 0 6.6 6.6l2.2-2.2a1 1 0 0 1 1-.25 11 11 0 0 0 3.6.6 1 1 0 0 1 1 1V20a1 1 0 0 1-1 1A17 17 0 0 1 3 4a1 1 0 0 1 1-1h3.5a1 1 0 0 1 1 1c0 1.25.2 2.45.6 3.6a1 1 0 0 1-.25 1z"/></svg>
  123−456−7890
</div>
<div class="btn foot-btn">Web 予約はこちら</div>

<table class="sched">
  <tr><th style="width:130px">診療時間</th><th>月</th><th>火</th><th>水</th><th>木</th><th>金</th><th>土</th><th>日</th></tr>
  <tr><td>9:00 〜 12:00</td><td>○</td><td>○</td><td>○</td><td>−</td><td>○</td><td>○</td><td>−</td></tr>
  <tr><td>14:00 〜 20:00</td><td>○</td><td>○</td><td>○</td><td>−</td><td>○</td><td>●</td><td>−</td></tr>
</table>
<div class="sched-note">休診日：木曜・日曜・祝日<br>● 土曜日は 17:00 まで</div>

<nav class="foot-nav">
  <a>HOME</a><a>初めての方へ</a><a>小児</a><a>一般</a><a>矯正</a><a>診療内容</a><a>コンセプト</a><a>アクセス</a>
</nav>
<div class="copyright">Copyright (C) 2019 All Rights Reserved.</div>

</body>
</html>
```